Marketing Flyer for Plumber Referals

8.5" x11" Layout should be landscape not portrait. Create a bold, eye-catching flyer that highlights earning potential from referrals for water damage restoration. Use high-contrast colors like blue, yellow, and white, with bold fonts and dynamic layouts. Include images of restoration work, cash, and happy clients. Emphasize key benefits like $500 minimum payouts, fast payments, and unlimited income potential. Keep instructions simple: refer a client, we handle the work, you get paid. Add a clear call-to-action and display contact details prominently. Focus on professionalism and energy.

Target Market(s)

Plumbers and Contractor 8.5" x11" Layout should be landscape not portrait.

Industry/Entity Type

General Contractor

Colors
0054AA
0677BA
7BADD7
CADEEF
E8F1F8
EB3D1F
EC4F4E
F09395
F8D3D4
FCEDEE

Requirements
Must have
• 8.5" x11" Layout should be landscape not portrait.
Nice to have

```html
<!DOCTYPE html>
<html lang="en">
<head>
<meta charset="utf-8">
<title>Referral Flyers – Harborline Restore</title>
<link href="https://fonts.googleapis.com/css2?family=Poppins:wght@400;500;600;700;800;900&display=swap" rel="stylesheet">
<style>
  :root{
    --stage:#7b7b7b;
    --navy:#0b2a6e;
    --royal:#0e3a90;
    --ink:#1c1c1c;
    --yellow:#ffe100;
    --red:#d8262a;
    --red-soft:#e03a3a;
    --white:#ffffff;
    --link-blue:#1559d6;
    --dark-pill:#262626;
  }
  *{margin:0;padding:0;box-sizing:border-box}
  html,body{width:833px;height:1200px;overflow:hidden}
  body{background:var(--stage);font-family:"Poppins",sans-serif;position:relative}
  .flyer{position:absolute;left:93px;width:647px;height:499px;background:var(--white);overflow:hidden;box-shadow:0 2px 6px rgba(0,0,0,.25)}
  .flyer--earn{top:71px}
  .flyer--steps{top:624px}
  .abs{position:absolute}
  .hero-art{position:absolute;left:0;top:0}
  .brand{position:absolute;text-align:center;color:var(--white);font-weight:500;font-size:12px;letter-spacing:1.2px;white-space:nowrap}
  .brand-mark{display:block;width:12px;height:12px;border:1.5px solid var(--white);margin:0 auto 6px}
  .headline{position:absolute;font-weight:800;line-height:1;text-align:center;white-space:nowrap}
  .headline--earn{left:0;width:335px;top:96px;font-size:52px;color:var(--yellow)}
  .headline--unlimited{left:0;width:335px;top:144px;font-size:36px;color:var(--white)}
  .headline--cash{left:0;width:335px;top:180px;font-size:36px;color:var(--white)}
  .bar-text{position:absolute;font-weight:800;color:var(--navy);white-space:nowrap}
  .bar-text--flood{left:50px;top:222px;font-size:20px}
  .payout{position:absolute;left:37px;top:272px;width:307px;height:43px}
  .payout-amount{position:absolute;color:var(--white);font-weight:800;line-height:1}
  .why-title{position:absolute;left:43px;top:326px;font-size:16px;font-weight:800;color:var(--navy)}
  .benefit{position:absolute;top:348px;width:96px;height:67px;border:2px solid var(--navy);border-radius:9px 9px 9px 9px;background:var(--white)}
  .benefit-head{position:absolute;left:4px;top:3px;width:84px;height:24px;border:2px solid var(--royal);border-radius:12px;background:var(--white);display:flex;align-items:center;justify-content:center;text-align:center;font-size:7.5px;font-weight:700;line-height:1.05;color:var(--navy);text-transform:uppercase}
  .benefit-body{position:absolute;left:8px;top:34px;width:60px;font-size:5.6px;font-weight:600;line-height:1.3;color:var(--ink)}
  .benefit-body em{font-style:normal;color:var(--link-blue)}
  .benefit-icon{position:absolute;right:5px;top:33px}
  .slogan{position:absolute;left:40px;top:422px;font-size:19px;font-weight:800;color:var(--navy);white-space:nowrap;letter-spacing:-.2px}
  .slogan span{color:var(--red)}
  .footer{position:absolute;left:0;bottom:0;width:647px;height:40px}
  .footer-cta{position:absolute;left:46px;top:11px;font-size:13px;font-weight:700;color:var(--white);white-space:nowrap}
  .footer-cta small{font-size:13px;font-weight:400}
  .footer-phone{position:absolute;left:309px;top:5px;font-size:19px;font-weight:700;color:var(--ink);letter-spacing:.5px}
  .footer-web{position:absolute;left:480px;top:12px;font-size:11px;font-weight:700;color:var(--ink)}
  .headline--refer{left:47px;top:116px;font-size:32px;color:var(--white);text-align:left;line-height:1.02}
  .bar-text--how{left:61px;top:205px;font-size:21px}
  .step{position:absolute;top:254px;width:174px;height:183px;border:2px solid var(--navy);border-radius:10px;overflow:hidden;background:var(--white)}
  .step-art{position:absolute;left:0;top:0;width:100%;height:93px;border-bottom:2px solid var(--navy);border-radius:0 0 10px 10px}
  .step-title{position:absolute;left:0;width:100%;top:104px;text-align:center;font-size:12.5px;font-weight:800;line-height:1.05;color:var(--navy)}
  .step-body{position:absolute;left:0;width:100%;top:136px;text-align:center;font-size:9.5px;font-weight:500;line-height:1.25;color:var(--ink)}
  .step-body em{font-style:normal;font-weight:600;color:var(--link-blue)}
</style>
</head>
<body>

<!-- Flyer 1: Earn -->
<section class="flyer flyer--earn">
  <svg class="hero-art" width="647" height="262" viewBox="0 0 647 262">
    <defs>
      <linearGradient id="blueFade" x1="0" y1="0" x2="1" y2="1">
        <stop offset="0" stop-color="#0f3d96"/><stop offset="1" stop-color="#0a2c74"/>
      </linearGradient>
      <linearGradient id="floodPhoto" x1="0" y1="0" x2="0" y2="1">
        <stop offset="0" stop-color="#e8e8e6"/><stop offset=".45" stop-color="#bdb9b0"/><stop offset="1" stop-color="#8f949a"/>
      </linearGradient>
    </defs>
    <rect width="647" height="262" fill="url(#blueFade)"/>
    <polygon role="img" aria-label="Photo of a flooded home interior with a staircase standing in water" points="376,0 647,0 647,262 362,262 326,118" fill="url(#floodPhoto)"/>
    <polyline points="376,0 326,118 362,262" fill="none" stroke="#fff" stroke-width="4"/>
    <polygon points="40,218 386,218 402,251 40,251" fill="var(--yellow)"/>
  </svg>

  <div class="brand" style="left:83px;top:62px;width:140px"><i class="brand-mark"></i>HARBORLINE RESTORE</div>
  <div class="headline headline--earn">EARN</div>
  <div class="headline headline--unlimited">UNLIMITED</div>
  <div class="headline headline--cash">CASH</div>
  <div class="bar-text bar-text--flood">GET PAID TO REFER A FLOOD</div>

  <svg class="payout" viewBox="0 0 307 43">
    <rect x="0" y="0" width="307" height="43" rx="21.5" fill="var(--red-soft)"/>
    <rect x="120" y="0" width="187" height="43" rx="21.5" fill="var(--red)"/>
    <circle cx="117" cy="21.5" r="21" fill="#fff"/>
  </svg>
  <div class="payout-amount" style="left:59px;top:275px;font-size:22px"><sup style="font-size:11px">$</sup>500</div>
  <div class="payout-amount" style="left:52px;top:297px;font-size:12px">MINIMUM</div>
  <div class="payout-amount" style="left:140px;top:283px;font-size:16px;color:var(--navy)">OR</div>
  <div class="payout-amount" style="left:180px;top:276px;font-size:33px">10%</div>
  <div class="payout-amount" style="left:246px;top:279px;font-size:14px;line-height:.95">PER<br>REFERRAL!</div>

  <svg class="abs" style="left:370px;top:226px" width="260" height="120" viewBox="370 226 260 120">
    <rect x="451" y="279" width="169" height="34" rx="8" fill="var(--dark-pill)"/>
    <g fill="var(--navy)">
      <rect x="390" y="245" width="78" height="78" transform="rotate(0 429 284)"/>
      <rect x="390" y="245" width="78" height="78" transform="rotate(15 429 284)"/>
      <rect x="390" y="245" width="78" height="78" transform="rotate(30 429 284)"/>
      <rect x="390" y="245" width="78" height="78" transform="rotate(45 429 284)"/>
      <rect x="390" y="245" width="78" height="78" transform="rotate(60 429 284)"/>
      <rect x="390" y="245" width="78" height="78" transform="rotate(75 429 284)"/>
    </g>
    <path id="badgeArc" d="M386,294 A44,44 0 0 1 472,294" fill="none"/>
    <text font-family="Poppins,sans-serif" font-size="10" font-weight="600" fill="#fff" letter-spacing="1"><textPath href="#badgeArc" startOffset="50%" text-anchor="middle">PARTNER WITH THE</textPath></text>
    <text x="426" y="303" text-anchor="middle" font-family="Poppins,sans-serif" font-size="33" font-weight="900" fill="#fff">#1</text>
    <text x="484" y="294" font-family="Poppins,sans-serif" font-size="9.5" font-weight="700" fill="#fff">WATER DAMAGE</text>
    <text x="484" y="306" font-family="Poppins,sans-serif" font-size="9.5" font-weight="700" fill="#fff">RESTORATION TEAM</text>
  </svg>

  <div class="why-title">WHY PARTNER WITH US?</div>

  <div class="benefit" style="left:40px">
    <div class="benefit-head">Guaranteed<br>Payout</div>
    <div class="benefit-body">Minimum <em>$500 or 10%</em> of the invoice, paid fast.</div>
    <svg class="benefit-icon" width="26" height="26" viewBox="0 0 26 26"><circle cx="13" cy="13" r="11" fill="none" stroke="var(--ink)" stroke-width="1.3"/><path d="M8 13.5l3.5 3.5 7-7" fill="none" stroke="var(--ink)" stroke-width="1.5"/></svg>
  </div>
  <div class="benefit" style="left:160px">
    <div class="benefit-head">Free<br>Evaluations</div>
    <div class="benefit-body">We assess damage and process insurance claims for your clients.</div>
    <svg class="benefit-icon" width="26" height="28" viewBox="0 0 26 28"><rect x="5" y="2" width="17" height="22" rx="1" fill="none" stroke="var(--ink)" stroke-width="1.3"/><path d="M9 8h9M9 12h9M9 16h6" stroke="var(--ink)" stroke-width="1.2"/></svg>
  </div>
  <div class="benefit" style="left:301px">
    <div class="benefit-head">Affordable<br>Solutions</div>
    <div class="benefit-body">Lowest out-of-pocket <em>costs for your customers.</em></div>
    <svg class="benefit-icon" width="26" height="28" viewBox="0 0 26 28"><circle cx="14" cy="11" r="8" fill="none" stroke="var(--ink)" stroke-width="1.3"/><text x="14" y="15" text-anchor="middle" font-size="11" font-weight="700" font-family="Poppins,sans-serif" fill="var(--ink)">$</text><path d="M2 26l6-6h10" fill="none" stroke="var(--ink)" stroke-width="1.3"/></svg>
  </div>
  <div class="benefit" style="left:426px">
    <div class="benefit-head">Industry<br>Leaders</div>
    <div class="benefit-body">Certified experts with <em>24/7 rapid</em> response</div>
    <svg class="benefit-icon" width="26" height="28" viewBox="0 0 26 28"><circle cx="13" cy="7" r="4.5" fill="none" stroke="var(--ink)" stroke-width="1.3"/><circle cx="6" cy="18" r="2.5" fill="none" stroke="var(--ink)" stroke-width="1.2"/><circle cx="20" cy="18" r="2.5" fill="none" stroke="var(--ink)" stroke-width="1.2"/><path d="M2 26a4 4 0 0 1 8 0M16 26a4 4 0 0 1 8 0" fill="none" stroke="var(--ink)" stroke-width="1.2"/></svg>
  </div>

  <svg class="abs" style="left:540px;top:318px" width="80" height="102" viewBox="540 318 80 102">
    <path d="M580,416 L553,384 A35,35 0 1 1 607,384 Z" fill="var(--navy)"/>
    <circle cx="580" cy="336" r="8" fill="none" stroke="var(--red)" stroke-width="2"/>
    <path d="M576 336l3 3 5-6" fill="none" stroke="var(--red)" stroke-width="1.6"/>
    <text x="580" y="368" text-anchor="middle" font-family="Poppins,sans-serif" font-size="23" font-weight="800" fill="#fff">24/7</text>
    <text x="580" y="383" text-anchor="middle" font-family="Poppins,sans-serif" font-size="10" font-weight="700" fill="#fff">RAPID</text>
    <rect x="547" y="387" width="66" height="13" fill="var(--red)"/>
    <text x="580" y="397.5" text-anchor="middle" font-family="Poppins,sans-serif" font-size="9.5" font-weight="800" fill="var(--yellow)">RESPONSE</text>
  </svg>

  <div class="slogan">SEND <span>REFERRALS</span>. GET <span>PAID</span>. GROW <span>YOUR BUSINESS.</span></div>

  <svg class="footer" viewBox="0 0 647 40">
    <polygon points="0,0 268,0 297,40 0,40" fill="var(--navy)"/>
    <circle cx="300" cy="17" r="7.5" fill="var(--ink)"/>
    <path d="M297 13.5c0 3 2.5 6 5.5 7l1.3-1.5-1.8-1.2-.9.8c-1-.5-2-1.5-2.5-2.5l.8-.9-1.2-1.8z" fill="#fff"/>
    <circle cx="466" cy="17" r="7.5" fill="var(--ink)"/>
    <ellipse cx="466" cy="17" rx="3" ry="6" fill="none" stroke="#fff" stroke-width=".9"/>
    <path d="M460 17h12" stroke="#fff" stroke-width=".9"/>
  </svg>
  <div class="footer-cta" style="top:470px">CALL TEXT <small>OR</small> BOOK ON-LINE</div>
  <div class="footer-phone" style="top:464px">555-010-4477</div>
  <div class="footer-web" style="top:471px">HarborlineRestore.com</div>
</section>

<!-- Flyer 2: How it works -->
<section class="flyer flyer--steps">
  <svg class="hero-art" width="647" height="240" viewBox="0 0 647 240">
    <defs>
      <linearGradient id="cashPhoto" x1="0" y1="0" x2="1" y2="1">
        <stop offset="0" stop-color="#cfd3cc"/><stop offset=".5" stop-color="#a9b2a6"/><stop offset="1" stop-color="#8e978c"/>
      </linearGradient>
    </defs>
    <rect width="647" height="214" fill="url(#blueFade)"/>
    <polygon role="img" aria-label="Photo of hundred-dollar bills with letter tiles spelling cash flow" points="320,0 647,0 647,214 365,214" fill="url(#cashPhoto)"/>
    <line x1="320" y1="0" x2="365" y2="214" stroke="#fff" stroke-width="4"/>
    <polygon points="0,203 279,203 295,238 0,238" fill="var(--yellow)"/>
  </svg>

  <div class="brand" style="left:87px;top:66px;width:140px"><i class="brand-mark"></i>HARBORLINE RESTORE</div>
  <div class="headline headline--refer">GET PAID TO<br>REFER A FLOOD</div>
  <div class="bar-text bar-text--how">HOW IT WORKS</div>

  <div class="step" style="left:47px">
    <div class="step-art" role="img" aria-label="Photo of a leaking white drain pipe" style="background:linear-gradient(135deg,#bfc3c6,#5a5f63)"></div>
    <div class="step-title">REFER FLOOD, WATER<br>AND MOLD DAMAGE</div>
    <div class="step-body" style="top:137px">Call, book online, or<br><em>text us directly.</em></div>
  </div>
  <div class="step" style="left:238px">
    <div class="step-art" role="img" aria-label="Affiliate marketing illustration with join, promote and earn icons" style="background:linear-gradient(135deg,#f4f4f4,#c9d4dc)"></div>
    <div class="step-title">WE TAKE CARE OF<br>EVERYTHING</div>
    <div class="step-body"><em>Free evaluations,</em><br>insurance claims,<br>and professional service.</div>
  </div>
  <div class="step" style="left:424px">
    <div class="step-art" role="img" aria-label="Yellow road sign reading get paid to share against a blue sky" style="background:linear-gradient(135deg,#dfe9f3,#4f86c6)"></div>
    <div class="step-title">WE TAKE CARE OF<br>EVERYTHING</div>
    <div class="step-body"><em>$500 minimum or 10% of the</em><br>invoice within 48 hours of<br>final payment.</div>
  </div>

  <svg class="footer" viewBox="0 0 647 40">
    <polygon points="0,0 268,0 297,40 0,40" fill="var(--navy)"/>
    <circle cx="300" cy="17" r="7.5" fill="var(--ink)"/>
    <path d="M297 13.5c0 3 2.5 6 5.5 7l1.3-1.5-1.8-1.2-.9.8c-1-.5-2-1.5-2.5-2.5l.8-.9-1.2-1.8z" fill="#fff"/>
    <circle cx="466" cy="17" r="7.5" fill="var(--ink)"/>
    <ellipse cx="466" cy="17" rx="3" ry="6" fill="none" stroke="#fff" stroke-width=".9"/>
    <path d="M460 17h12" stroke="#fff" stroke-width=".9"/>
  </svg>
  <div class="footer-cta" style="top:470px">CALL TEXT <small>OR</small> BOOK ON-LINE</div>
  <div class="footer-phone" style="top:464px">555-010-4477</div>
  <div class="footer-web" style="top:471px">HarborlineRestore.com</div>
</section>

</body>
</html>
```